Business Card

Need a clean, professional, simple, but clever business card for our company LUX RIDES. We only want to see black and white colors as that reflects the branding of our company. Attaching logo. Will also consider the "sky blue" shown in our web site sample png - but use of the color should be minimal.

Lux Rides is a executive car service operating in cities throughout Africa. By operating well equipped Valdren Oster vehicles, we offer the smoothest and stylish ride in town. We aim to provide customers with a valuable experience. That’s why we make sure our patrons get picked up like a boss, travel in style, and arrive fabulous.

We need a card that says that. Likely to print on the best quality/smoothest paper available, as it must speak volumes of our business and class.

We would like the rear of the card to be all black. Perhaps we can put the web url on it, or leave it blank if it looks neater/more elegant.

Use the following contact information (as you see fit):

Lux Rides Limited
P.O. Box 47106
Dar es Salaam, Tanzania

Baraka Kilonzo
Managing Director

+255 (0) 754 829016
sales@luxrides-demo.co.tz

web url: www.luxrides-demo.co.tz
email: chauffeur@luxrides-demo.co.tz

***Winning designer will likely be commissioned for more promotional work in near future.

Target Market(s)

The target market for this card is corporate executives of top firms (financial, consulting, businessmen, etc). They are interested in high quality transportation. Our fleet is all high end Valdren Oster black cars (black exterior, black interior); and therefore, that high end quality and promptness must be reflected in the card. Also simplicity, as we we take care of all the little details behind the scene.

Industry/Entity Type

Business

Requirements
Must have
• Font must be: Helvetica Neue, like the logo. You may use other variations (Thin, Ultra thin, Regular, Bold), so long as it looks and prints well.

If web url is included on the back of the card, then do NOT include it also on the front.
Nice to have
• If there is something nice and clever that you can do/think of that doesn't make the card look busy, but adds a little "posh", then I could be even more interested.

However, if there's no little thing do be done, I'd rather a simple, but very professional looking card that attracts a lot of attention.

```html
<!DOCTYPE html>
<html lang="en">
<head>
<meta charset="utf-8">
<title>Lux Rides – Business Card</title>
<link rel="stylesheet" href="https://fonts.googleapis.com/css2?family=Open+Sans:wght@300;400;600&display=swap">
<style>
  :root {
    --canvas-bg: #e9e7e4;
    --card-white: #ffffff;
    --card-black: #000000;
    --curve-edge: #4a4a4a;
    --ink: #1a1a1a;
    --ink-soft: #333333;
    --rule: #8a8a8a;
    --shadow: rgba(0, 0, 0, 0.18);
  }
  * { box-sizing: border-box; margin: 0; padding: 0; }
  html, body {
    width: 1200px;
    height: 900px;
    overflow: hidden;
    background: var(--canvas-bg);
    font-family: "Open Sans", "Helvetica Neue", Arial, sans-serif;
    color: var(--ink);
  }
  .canvas {
    position: relative;
    width: 1200px;
    height: 900px;
  }
  .card {
    position: absolute;
    top: 295px;
    width: 540px;
    height: 310px;
    box-shadow: 0 6px 18px var(--shadow);
    overflow: hidden;
  }
  .card-front { left: 45px; background: var(--card-white); }
  .card-back { left: 615px; background: var(--card-black); }

  .front-band {
    position: absolute;
    inset: 0;
    width: 540px;
    height: 310px;
  }

  .brand-name {
    position: absolute;
    left: 30px;
    top: 66px;
    font-weight: 300;
    font-size: 44px;
    letter-spacing: 3px;
    line-height: 1;
    color: var(--ink);
    white-space: nowrap;
  }
  .brand-rule {
    position: absolute;
    left: 30px;
    top: 124px;
    width: 300px;
    height: 1px;
    background: var(--rule);
  }

  .holder {
    position: absolute;
    left: 70px;
    top: 142px;
  }
  .holder-name {
    font-weight: 600;
    font-size: 19px;
    letter-spacing: 0.5px;
    line-height: 1.2;
    padding-bottom: 2px;
    border-bottom: 1px solid var(--ink);
    width: 270px;
    white-space: nowrap;
  }
  .holder-title {
    font-weight: 600;
    font-size: 11px;
    margin-top: 3px;
    margin-left: 10px;
  }

  .address {
    position: absolute;
    right: 334px;
    top: 236px;
    font-style: normal;
    font-weight: 300;
    font-size: 13px;
    line-height: 1.6;
    color: var(--ink-soft);
    text-align: right;
    white-space: nowrap;
  }

  .divider {
    position: absolute;
    left: 218px;
    top: 198px;
    width: 1px;
    height: 92px;
    background: var(--rule);
  }

  .contact-list {
    position: absolute;
    left: 230px;
    top: 202px;
    list-style: none;
  }
  .contact-item {
    display: flex;
    align-items: center;
    gap: 8px;
    font-weight: 300;
    font-size: 12px;
    line-height: 20px;
    color: var(--ink-soft);
    white-space: nowrap;
  }
  .contact-icon {
    width: 11px;
    height: 11px;
    flex: none;
  }
</style>
</head>
<body>
<main class="canvas">

  <section class="card card-front" aria-label="Business card front">
    <svg class="front-band" viewBox="0 0 540 310" aria-hidden="true">
      <path d="M392,0 C452,60 476,190 452,310 L540,310 L540,0 Z" fill="var(--card-black)"/>
      <path d="M392,0 C452,60 476,190 452,310" fill="none" stroke="var(--curve-edge)" stroke-width="5"/>
    </svg>

    <div class="brand-name">LUX RIDES</div>
    <div class="brand-rule"></div>

    <div class="holder">
      <div class="holder-name">Baraka Kilonzo</div>
      <div class="holder-title">Managing Director</div>
    </div>

    <address class="address">
      P.O. Box 47106<br>
      Dar es Salaam, Tanzania
    </address>

    <div class="divider"></div>

    <ul class="contact-list">
      <li class="contact-item">
        <svg class="contact-icon" viewBox="0 0 12 12" aria-hidden="true">
          <path d="M2.5 0.8 L4.6 0.8 L5.2 3.4 L3.8 4.3 C4.5 6 5.9 7.5 7.7 8.3 L8.6 6.9 L11.2 7.5 L11.2 9.6 C11.2 10.6 10.4 11.2 9.5 11.1 C5 10.6 1.4 7 0.9 2.5 C0.8 1.6 1.5 0.8 2.5 0.8 Z" fill="var(--ink)"/>
        </svg>
        <span>+255 (0) 754 829016</span>
      </li>
      <li class="contact-item">
        <svg class="contact-icon" viewBox="0 0 12 12" aria-hidden="true">
          <rect x="0.5" y="2.5" width="11" height="7.5" fill="var(--ink)"/>
          <path d="M0.8 2.8 L6 7 L11.2 2.8" fill="none" stroke="var(--card-white)" stroke-width="1"/>
        </svg>
        <span>sales@luxrides-demo.co.tz</span>
      </li>
      <li class="contact-item">
        <svg class="contact-icon" viewBox="0 0 12 12" aria-hidden="true">
          <rect x="0.5" y="2.5" width="11" height="7.5" fill="var(--ink)"/>
          <path d="M0.8 2.8 L6 7 L11.2 2.8" fill="none" stroke="var(--card-white)" stroke-width="1"/>
        </svg>
        <span>chauffeur@luxrides-demo.co.tz</span>
      </li>
      <li class="contact-item">
        <svg class="contact-icon" viewBox="0 0 12 12" aria-hidden="true">
          <circle cx="6" cy="6" r="5.2" fill="var(--ink)"/>
          <ellipse cx="6" cy="6" rx="2.2" ry="5.2" fill="none" stroke="var(--card-white)" stroke-width="0.8"/>
          <line x1="0.8" y1="6" x2="11.2" y2="6" stroke="var(--card-white)" stroke-width="0.8"/>
        </svg>
        <span>www.luxrides-demo.co.tz</span>
      </li>
    </ul>
  </section>

  <section class="card card-back" aria-label="Business card back"></section>

</main>
</body>
</html>
```